Visitenkarten-Design für Gesundheits- und Ernährungsberaterin
Zielgruppe
Ich bin Gesundheit und Ernährungsberaterin
Zielgruppe sind chronisch Kranke und Gesundheitsbewusste Personen
Aufgabenstellung
Schlichtes aber direkt erkennbares Design.
Mahl mit Maß , Gesundheit und Ernährungsberatung ( gut lesbar , elegant)
Marlene Obruk-Feistinger ( nicht so groß )
Grau ; Grün Töne und gerne etwas rosa
Infos wie Adresse und E-Mail vielleicht in jeweilige Blöcke am unteren Rand

```html
<!DOCTYPE html>
<html lang="de">
<head>
<meta charset="utf-8">
<title>Visitenkarten – Mahl mit Maß</title>
<link href="https://fonts.googleapis.com/css2?family=Montserrat:wght@400;600;700&display=swap" rel="stylesheet">
<style>
  :root{
    --green:#8dd35f;
    --green-light:#c5e8b0;
    --grey:#666666;
    --text-grey:#555555;
    --pink:#f0a6a6;
    --white:#ffffff;
    --page:#ffffff;
  }
  *{box-sizing:border-box;margin:0;padding:0}
  html,body{width:861px;height:1200px;overflow:hidden;background:var(--page)}
  body{position:relative;font-family:"Montserrat",Arial,sans-serif;text-transform:uppercase}
  .card{position:absolute;width:335px;height:220px;background:var(--white);overflow:hidden;
        box-shadow:4px 5px 6px rgba(0,0,0,.28)}
  .col-left{left:77px}.col-right{left:447px}
  .row-1{top:181px}.row-2{top:471px}.row-3{top:773px}
  .card--green{background:var(--green)}
  .card--grey{background:var(--grey)}
  .edge{position:absolute;left:0;top:0;bottom:0;width:10px}
  .edge--light{background:var(--green-light)}
  .edge--green{background:var(--green)}

  /* brand name in place of a mark */
  .brand{position:absolute;display:flex;align-items:center;gap:6px;font-weight:600;text-transform:none;white-space:nowrap}
  .brand__dot{width:20px;height:20px;border-radius:50%;background:currentColor;flex:none}
  .brand--back{left:10px;right:0;top:55px;justify-content:center;font-size:20px}
  .brand--front{right:10px;top:34px;font-size:13px}
  .brand--front .brand__dot{width:14px;height:14px}
  .brand--white{color:var(--white)}
  .brand--green{color:var(--green)}

  .claim{position:absolute;left:10px;right:0;text-align:center;letter-spacing:.08em}
  .claim--small{top:158px;font-size:8.4px;line-height:11px;color:var(--white)}
  .claim--large{top:164px;font-size:12.5px;color:var(--pink)}
  .claim--large.is-green{color:var(--green);left:0;top:170px}
  .tagline{position:absolute;right:9px;top:95px;font-size:9px;letter-spacing:.06em}
  .tagline--green{color:var(--green)}
  .tagline--pink{color:var(--pink)}

  .person{position:absolute;left:18px;top:138px}
  .person__name{font-weight:700;font-size:10.5px;line-height:12px}
  .person__role{font-size:6.2px;line-height:8px}
  .person--green{color:var(--green)}
  .person--grey{color:var(--text-grey)}

  .address{position:absolute;left:18px;bottom:6px;font-size:8.2px;line-height:10.5px}
  .contact{position:absolute;left:163px;bottom:6px;font-size:8.2px;line-height:10.5px;border-collapse:collapse}
  .contact th{font-weight:400;text-align:left;width:34px;padding:0}
  .contact td{padding:0;white-space:nowrap}
  .info--green{color:var(--green)}
  .info--grey{color:var(--text-grey)}

  .card--waves .person{top:126px}
  .card--waves .address,.card--waves .contact{bottom:auto;top:164px}
  .card--waves .tagline{top:102px}
  .card--waves .brand--front{top:40px}
  .wave{position:absolute;left:0;width:335px;height:32px}
  .wave--top{top:0}
  .wave--bottom{bottom:0;transform:scaleY(-1)}
  .wave__dark{fill:var(--green)}
  .wave__light{fill:var(--green-light)}
</style>
</head>
<body>

  <!-- Variant 1 -->
  <section class="card card--green col-left row-1">
    <div class="edge edge--light"></div>
    <div class="brand brand--back brand--white"><span class="brand__dot"></span>Mahl mit Maß</div>
    <p class="claim claim--small">Mahl mit Maß , Gesundheits-<br>und Ernährungsberatung.</p>
  </section>
  <section class="card col-right row-1">
    <div class="edge edge--light"></div>
    <div class="brand brand--front brand--green"><span class="brand__dot"></span>Mahl mit Maß</div>
    <p class="tagline tagline--green">Mahl mit Maß.</p>
    <div class="person person--green">
      <p class="person__name">Marlene Obruk-Feistinger</p>
      <p class="person__role">Gesundheits- und Ernährungsberaterin</p>
    </div>
    <p class="address info--green">Lindenwinkel 4<br>24790 Wiesenfelde</p>
    <table class="contact info--green">
      <tr><th>Tel</th><td>04512 /604 27 19</td></tr>
      <tr><th>Mobil</th><td>0157 / 23 48 61 05</td></tr>
      <tr><th>Mail</th><td>beratung-mof@postfach.de</td></tr>
    </table>
  </section>

  <!-- Variant 2 -->
  <section class="card card--grey col-left row-2">
    <div class="edge edge--green"></div>
    <div class="brand brand--back brand--green"><span class="brand__dot"></span>Mahl mit Maß</div>
    <p class="claim claim--large">Mahl mit Maß.</p>
  </section>
  <section class="card col-right row-2">
    <div class="edge edge--green"></div>
    <div class="brand brand--front brand--green"><span class="brand__dot"></span>Mahl mit Maß</div>
    <p class="tagline tagline--pink">Mahl mit Maß.</p>
    <div class="person person--grey">
      <p class="person__name">Marlene Obruk-Feistinger</p>
      <p class="person__role">Gesundheits- und Ernährungsberaterin</p>
    </div>
    <p class="address info--grey">Lindenwinkel 4<br>24790 Wiesenfelde</p>
    <table class="contact info--grey">
      <tr><th>Tel</th><td>04512 /604 27 19</td></tr>
      <tr><th>Mobil</th><td>0157 / 23 48 61 05</td></tr>
      <tr><th>Mail</th><td>beratung-mof@postfach.de</td></tr>
    </table>
  </section>

  <!-- Variant 3 -->
  <section class="card card--waves col-left row-3">
    <svg class="wave wave--top" viewBox="0 0 335 32" aria-hidden="true">
      <path class="wave__dark" d="M0 0H300C200 7 100 11 0 11Z"/>
      <path class="wave__light" d="M0 14C120 14 250 8 335 0C250 14 120 27 0 29Z"/>
    </svg>
    <div class="brand brand--back brand--green" style="top:60px"><span class="brand__dot"></span>Mahl mit Maß</div>
    <p class="claim claim--large is-green">Mahl mit Maß.</p>
    <svg class="wave wave--bottom" viewBox="0 0 335 32" aria-hidden="true">
      <path class="wave__dark" d="M0 0H300C200 7 100 11 0 11Z"/>
      <path class="wave__light" d="M0 14C120 14 250 8 335 0C250 14 120 27 0 29Z"/>
    </svg>
  </section>
  <section class="card card--waves col-right row-3">
    <svg class="wave wave--top" viewBox="0 0 335 32" aria-hidden="true">
      <path class="wave__dark" d="M0 0H300C200 7 100 11 0 11Z"/>
      <path class="wave__light" d="M0 14C120 14 250 8 335 0C250 14 120 27 0 29Z"/>
    </svg>
    <div class="brand brand--front brand--green"><span class="brand__dot"></span>Mahl mit Maß</div>
    <p class="tagline tagline--green">Mahl mit Maß.</p>
    <div class="person person--green">
      <p class="person__name">Marlene Obruk-Feistinger</p>
      <p class="person__role">Gesundheits- und Ernährungsberaterin</p>
    </div>
    <p class="address info--green">Lindenwinkel 4<br>24790 Wiesenfelde</p>
    <table class="contact info--green">
      <tr><th>Tel</th><td>04512 /604 27 19</td></tr>
      <tr><th>Mobil</th><td>0157 / 23 48 61 05</td></tr>
      <tr><th>Mail</th><td>beratung-mof@postfach.de</td></tr>
    </table>
    <svg class="wave wave--bottom" viewBox="0 0 335 32" aria-hidden="true">
      <path class="wave__dark" d="M0 0H300C200 7 100 11 0 11Z"/>
      <path class="wave__light" d="M0 14C120 14 250 8 335 0C250 14 120 27 0 29Z"/>
    </svg>
  </section>

</body>
</html>
```